Web Design Project

The aim of this project to design a website for a service that would offer services for small business and non profit organizations using opensource software that is weaved to work together in harmony.

The website name is: velisto.net

Velisto in Arabic means: cabbage. Cabbage is composed of leaves, actually there is nothing except leaves. Each leave by itself is not called cabbage, but a collection of leaves that are organized in a central way would give us cabbage.

Same idea for Velisto where open source software very well organized and integrated would create a new thing with a new value.
Updates

Target Market(s)

Small business, Europe, Africa, Far east and Middle east

Industry/Entity Type

Small Business

Requirements
Must have
• The website would offer the following sections:
* Home page
* Benefits: value of velisto
* Applications: applications offered by velisto
* Pricing
* Purchase
* Customer log in
* Support
- FAQ
- Knowledge base
- Forums
- Open tickets

Please take the following consideration in design:
* White should predominate
* Only black and the colors of logo are permitted (attched)
Nice to have
• Design is better to express:
* Openness
* Dynamic
* Usable
* Cost effective

Files

```html
<!DOCTYPE html>
<html lang="en">
<head>
<meta charset="utf-8">
<title>Velisto – Solutions for Small Business and NPOs</title>
<link href="https://fonts.googleapis.com/css2?family=Raleway:wght@300;400;600;700&family=Arimo:wght@400;700&display=swap" rel="stylesheet">
<style>
:root{
  --magenta:#b0468d;
  --magenta-dark:#8f3472;
  --cyan:#27a6d8;
  --ink:#111111;
  --text:#666a6e;
  --topbar:#3d4246;
  --hero-bg-1:#f4f5f6;
  --hero-bg-2:#e3e6e8;
  --line:#d6dadd;
  --white:#ffffff;
}
*{box-sizing:border-box;margin:0;padding:0}
html,body{width:1022px;height:1200px;overflow:hidden;background:var(--white)}
body{position:relative;font-family:Arimo,Arial,sans-serif;color:var(--text)}
.abs{position:absolute}

/* top bar */
.topbar{left:0;top:0;width:1022px;height:38px;background:var(--topbar);border-bottom:2px solid #5b6167}
.topbar-links{left:132px;top:14px;font:700 8px Raleway,sans-serif;letter-spacing:.4px;color:#d9dcde}
.topbar-links span{padding:0 6px;border-right:1px solid #7b8086}
.topbar-links span:first-child{padding-left:0}
.social{top:8px;display:flex;gap:6px;left:760px}
.social i{display:block;width:22px;height:22px;background:#1d2023;border:1px solid #6a7075}
.social i.wide{width:36px}

/* nav */
.navbar{left:0;top:38px;width:1022px;height:72px;border-bottom:1px solid #e4e6e8;background:var(--white)}
.brand{left:142px;top:62px;display:flex;align-items:center;gap:8px;font:600 20px Raleway,sans-serif;color:var(--ink)}
.brand b{display:block;width:18px;height:18px;border-radius:50%;background:var(--magenta)}
.nav{top:38px;left:0;font:700 11px Raleway,sans-serif;letter-spacing:.3px;color:#222}
.nav a{position:absolute;top:0;padding-top:30px;height:56px;color:#222;text-decoration:none;white-space:nowrap}
.nav a.active{color:var(--cyan);border-top:3px solid var(--cyan);padding-top:27px}

/* hero */
.hero{left:0;top:113px;width:1022px;height:358px;background:linear-gradient(90deg,var(--hero-bg-1),#fafafa 45%,var(--hero-bg-2));border-bottom:1px solid var(--line)}
.hero-rule{left:0;top:116px;width:66px;height:2px;background:#cfd3d6}
.hero-photo{left:600px;top:113px;width:422px;height:358px;background:radial-gradient(ellipse at 60% 45%,#e2c9a8 0%,#cfc4bf 35%,#e6e8ea 75%)}
.hero-title{left:170px;top:172px;font:400 26px Arimo,Arial,sans-serif;color:var(--magenta);letter-spacing:-.3px}
.hero-sub{left:170px;top:224px;font:400 17px Arimo,Arial,sans-serif;color:var(--ink)}
.hero-copy{left:170px;top:258px;width:400px;font:700 11.6px/15px Arimo,Arial,sans-serif;color:#5e6266}
.btn{left:170px;top:370px;width:82px;height:26px;background:var(--magenta);border-bottom:2px solid var(--magenta-dark);border-radius:2px;color:var(--white);font:700 11px/25px Arimo,Arial,sans-serif;text-align:center}
.arrow{top:274px;width:34px;height:34px;border-radius:50%;background:#3b3e41}
.arrow.prev{left:8px}.arrow.next{left:984px}
.arrow svg{position:absolute;left:10px;top:10px}
.dots{left:488px;top:443px;display:flex;gap:6px}
.dots i{display:block;width:13px;height:13px;border-radius:50%;background:#c9cccf;border:2px solid #e7e9eb}
.dots i.on{background:#555a5e}

/* features */
.feature{top:530px;width:220px;margin-left:-110px;text-align:center}
.feature svg{display:block;margin:0 auto}
.feature h3{margin-top:20px;font:600 15px Raleway,sans-serif;color:var(--magenta)}
.feature p{margin-top:9px;font:400 12.5px/15px Arimo,Arial,sans-serif;color:var(--text)}
.feature a{display:block;margin-top:16px;font:400 12.5px Arimo,Arial,sans-serif;color:var(--cyan);text-decoration:none}

/* process */
.process-title{left:0;top:782px;width:1022px;text-align:center;font:300 35px Raleway,sans-serif;color:var(--ink);letter-spacing:-.8px}
.process-line{left:0;top:840px}
.step{top:946px;width:150px;margin-left:-75px;text-align:center}
.step h4{font:700 14px Raleway,sans-serif;color:var(--magenta)}
.step p{margin-top:7px;font:400 10.5px/18px Arimo,Arial,sans-serif;color:#6b6f73}

/* call to action */
.cta{left:0;top:1118px;width:1022px;text-align:center;font:400 23px Raleway,sans-serif;color:#4a4d50}
.cta strong{font-weight:700;color:var(--cyan)}
.to-top{left:982px;top:1103px;width:26px;height:24px;background:#8e9498;border:1px solid #b7bcbf;border-radius:2px}
.to-top svg{position:absolute;left:6px;top:7px}
</style>
</head>
<body>

<header>
  <div class="abs topbar"></div>
  <div class="abs topbar-links"><span>CUSTOMER LOGIN</span><span>CONTACT</span></div>
  <div class="abs social"><i></i><i></i><i class="wide"></i><i></i><i></i></div>

  <div class="abs navbar"></div>
  <div class="abs brand"><b></b>velisto</div>
  <nav class="abs nav">
    <a class="active" style="left:354px">HOME</a>
    <a style="left:430px">BENEFITS</a>
    <a style="left:524px">APPLICATIONS</a>
    <a style="left:644px">PRICING</a>
    <a style="left:732px">PURCHASE</a>
  </nav>
</header>

<section>
  <div class="abs hero"></div>
  <div class="abs hero-rule"></div>
  <div class="abs hero-photo" role="img" aria-label="Photo of a smiling woman pointing upward"></div>
  <h1 class="abs hero-title">Solutions for Small Business and NPOs</h1>
  <p class="abs hero-sub">Velisto makes it as simple as 1.2.3.</p>
  <p class="abs hero-copy">Lorem Ipsum is simply dummy text of the printing and typesetting industry. Lorem Ipsum has been the industry's standard dummy text ever since the 1500s, when an unknown printer took a galley of type and scrambled it to make a type specimen book. It has survived not only five centuries, but also the leap into electronic typesetting, remaining essentially unchanged.</p>
  <div class="abs btn">Blue Button</div>
  <div class="abs arrow prev"><svg width="14" height="14" viewBox="0 0 14 14"><path d="M9 2 L4 7 L9 12" fill="none" stroke="#fff" stroke-width="2"/></svg></div>
  <div class="abs arrow next"><svg width="14" height="14" viewBox="0 0 14 14"><path d="M5 2 L10 7 L5 12" fill="none" stroke="#fff" stroke-width="2"/></svg></div>
  <div class="abs dots"><i class="on"></i><i></i><i></i></div>
</section>

<section>
  <div class="abs feature" style="left:240px">
    <svg width="40" height="40" viewBox="0 0 40 40" role="img" aria-label="Question icon"><circle cx="20" cy="20" r="15" fill="none" stroke="var(--cyan)" stroke-width="2"/><text x="20" y="27" text-anchor="middle" font-family="Arimo,Arial,sans-serif" font-weight="700" font-size="19" fill="var(--magenta)">?</text></svg>
    <h3>Why Velisto?</h3>
    <p>Lorem ipsum dolor sit amet,<br>consectetur adipisicing elit mobile<br>devices.</p>
    <a>Learn More ›</a>
  </div>
  <div class="abs feature" style="left:504px">
    <svg width="40" height="40" viewBox="0 0 40 40" role="img" aria-label="Cart icon"><path d="M5 11 H10 L14 27 H31 L34 15 H12" fill="none" stroke="var(--cyan)" stroke-width="2.2" stroke-linejoin="round"/><circle cx="16" cy="32" r="2.5" fill="var(--cyan)"/><circle cx="29" cy="32" r="2.5" fill="var(--cyan)"/></svg>
    <h3>Buy Now</h3>
    <p>Lorem ipsum dolor sit amet,<br>consectetur adipisicing elit mobile<br>devices.</p>
    <a>Learn More ›</a>
  </div>
  <div class="abs feature" style="left:778px">
    <svg width="40" height="40" viewBox="0 0 40 40" role="img" aria-label="Document icon"><path d="M13 4 H27 L32 9 V34 H13 Z" fill="none" stroke="var(--cyan)" stroke-width="2"/><path d="M17 14 H28 M17 19 H28 M17 24 H28" stroke="var(--cyan)" stroke-width="1.6"/><path d="M4 12 H10 M6 17 H10 M4 22 H10" stroke="#e0453b" stroke-width="2"/></svg>
    <h3>User Guide</h3>
    <p>Lorem ipsum dolor sit amet,<br>consectetur adipisicing elit mobile<br>devices.</p>
    <a>Learn More ›</a>
  </div>
</section>

<section>
  <h2 class="abs process-title">How we do?</h2>
  <svg class="abs process-line" width="1022" height="290" viewBox="0 0 1022 290">
    <g stroke="#d3d7db" stroke-width="2" stroke-dasharray="6 4" fill="none">
      <path d="M126 48 H166"/><path d="M234 48 H321"/><path d="M389 48 H475"/><path d="M543 48 H630"/><path d="M698 48 H783"/><path d="M851 48 H894"/>
    </g>
    <g fill="#d3d7db">
      <path d="M158 43 L166 48 L158 53Z"/><path d="M313 43 L321 48 L313 53Z"/><path d="M467 43 L475 48 L467 53Z"/><path d="M622 43 L630 48 L622 53Z"/><path d="M775 43 L783 48 L775 53Z"/>
    </g>
    <g fill="#fff" stroke="#1f8fcf" stroke-width="2.5">
      <circle cx="200" cy="48" r="34"/><circle cx="355" cy="48" r="34"/><circle cx="509" cy="48" r="34"/><circle cx="664" cy="48" r="34"/><circle cx="817" cy="48" r="34"/>
    </g>
    <circle cx="200" cy="48" r="13" fill="#3fa6d8" role="img" aria-label="Understand icon"/>
    <circle cx="355" cy="48" r="13" fill="#f2a51c" role="img" aria-label="Think icon"/>
    <circle cx="509" cy="48" r="13" fill="#d8372f" role="img" aria-label="Develop icon"/>
    <circle cx="664" cy="48" r="13" fill="#b0468d" role="img" aria-label="Customize icon"/>
    <circle cx="817" cy="48" r="13" fill="#7fa844" role="img" aria-label="Implement icon"/>
    <path d="M126 216 Q126 240 150 240 H488 Q505 240 511 262 Q517 240 534 240 H872 Q894 240 894 216" fill="none" stroke="#d8dcdf" stroke-width="1.5" stroke-dasharray="2 3"/>
  </svg>
  <div class="abs step" style="left:200px"><h4>Understand</h4><p>Scenester cred you<br>probably haven't heard of<br>them, vinyl craft beer blog<br>stumptown</p></div>
  <div class="abs step" style="left:355px"><h4>Think</h4><p>Scenester cred you<br>probably haven't heard of<br>them, vinyl craft beer blog<br>stumptown</p></div>
  <div class="abs step" style="left:509px"><h4>Develop</h4><p>Scenester cred you<br>probably haven't heard of<br>them, vinyl craft beer blog<br>stumptown</p></div>
  <div class="abs step" style="left:664px"><h4>Customize</h4><p>Scenester cred you<br>probably haven't heard of<br>them, vinyl craft beer blog<br>stumptown</p></div>
  <div class="abs step" style="left:817px"><h4>Implement</h4><p>Scenester cred you<br>probably haven't heard of<br>them, vinyl craft beer blog<br>stumptown</p></div>
</section>

<section>
  <p class="abs cta">Do you like our Services? <strong>Contact Now</strong> <span style="color:var(--cyan);font-size:17px">›</span></p>
  <div class="abs to-top"><svg width="14" height="10" viewBox="0 0 14 10"><path d="M2 8 L7 3 L12 8" fill="none" stroke="#fff" stroke-width="2"/></svg></div>
</section>

</body>
</html>
```